Real Estate Sales Brokerage

Design a modern and fresh looking standard size business card, incorporate our logo's color scheme and modern appearance with head shot photo on front side and incorporate our log on the back side

Target Market(s)

Residential Home sales

Industry/Entity Type

Real Estate Agent

Font styles to use
Sans Serif

Colors

Designer to choose colors to be used in the design.

Requirements
Must have
• fresh, modern, not too busy, incorporate head shot in front of the card, incorporate logo in front and back of the card. Use logo design scheme as appropriate.
Nice to have
• horizontal and vertical options to compare would be nice.

```html
<!DOCTYPE html>
<html lang="en">
<head>
<meta charset="utf-8">
<title>Harbor Crest Realty – Business Card</title>
<link rel="stylesheet" href="https://fonts.googleapis.com/css2?family=Arimo:wght@400;700&display=swap">
<style>
  :root {
    --backdrop: #2a2a2a;
    --olive: #636034;
    --gold: #f2d64b;
    --paper: #ffffff;
    --ink: #555555;
    --photo-top: #c9ced3;
    --photo-bottom: #2f4f86;
  }
  * { margin: 0; padding: 0; box-sizing: border-box; }
  html, body { width: 1200px; height: 960px; overflow: hidden; }
  body {
    position: relative;
    background: var(--backdrop);
    font-family: "Arimo", Arial, sans-serif;
  }
  .card { position: absolute; width: 600px; height: 343px; overflow: hidden; }
  .card--front { left: 314px; top: 113px; background: var(--paper); }
  .card--back { left: 311px; top: 472px; background: var(--olive); }

  .brand { position: absolute; display: flex; align-items: center; }
  .brand__mark { flex: none; }
  .brand__name {
    font-weight: 400;
    text-transform: uppercase;
    line-height: 1.05;
  }
  .card--front .brand { left: 40px; top: 40px; gap: 18px; }
  .card--front .brand__mark { width: 58px; height: 58px; background: var(--olive); }
  .card--front .brand__name { color: var(--olive); font-size: 21px; }
  .card--back .brand { left: 214px; top: 105px; gap: 22px; }
  .card--back .brand__mark { width: 74px; height: 74px; background: var(--paper); }
  .card--back .brand__name { color: var(--paper); font-size: 28px; }

  .address {
    position: absolute; left: 46px; top: 184px;
    font-size: 14px; line-height: 18px; color: var(--ink);
  }
  .contacts {
    position: absolute; left: 46px; top: 230px;
    list-style: none; font-size: 14px; line-height: 19px; color: var(--ink);
  }
  .contacts li { display: flex; align-items: center; gap: 8px; }
  .contacts svg { width: 14px; height: 14px; fill: var(--olive); flex: none; }

  .headshot {
    position: absolute; left: 426px; top: 72px; width: 120px; height: 151px;
    border-radius: 6px;
    background: linear-gradient(180deg, var(--photo-top) 0%, var(--photo-top) 40%, var(--photo-bottom) 75%);
  }
  .nameplate { position: absolute; left: 343px; top: 248px; width: 257px; height: 65px; }
  .nameplate svg { position: absolute; inset: 0; }
  .nameplate__text { position: absolute; left: 60px; right: 0; top: 11px; text-align: center; }
  .nameplate__name { font-size: 20px; font-weight: 700; color: var(--gold); line-height: 24px; }
  .nameplate__title { font-size: 15px; color: var(--paper); line-height: 20px; }

  .website {
    position: absolute; left: 0; right: 0; top: 286px; text-align: center;
    font-size: 15px; letter-spacing: 4.2px; color: var(--paper);
  }
</style>
</head>
<body>

<section class="card card--front">
  <div class="brand">
    <span class="brand__mark"></span>
    <span class="brand__name">Harbor<br>Crest<br>Realty</span>
  </div>

  <p class="address">1420 Willow Bend Road<br>Fairbanks, Alaska 99701</p>

  <ul class="contacts">
    <li>
      <svg viewBox="0 0 16 16"><path d="M1 6c0-2 3-4 7-4s7 2 7 4v1h-3V5.5C11 5 10 4.5 8 4.5S5 5 4 5.5V7H1zM3 8h10l1 6H2zM8 9a2 2 0 1 0 0 4 2 2 0 0 0 0-4z"/></svg>
      <span>555 214 7730</span>
    </li>
    <li>
      <svg viewBox="0 0 16 16"><path d="M4 1h8v14H4zM5.5 3v9h5V3zM8 12.6a.8.8 0 1 0 0 1.6.8.8 0 0 0 0-1.6z"/></svg>
      <span>555 386 1942</span>
    </li>
    <li>
      <svg viewBox="0 0 16 16"><path d="M1 4h14v1L8 9 1 5zM1 6.5l7 4 7-4V12H1z"/></svg>
      <span>name@harborcrestrealty.com</span>
    </li>
    <li>
      <svg viewBox="0 0 16 16"><circle cx="8" cy="8" r="6.5"/></svg>
      <span>www.harborcrestrealty.com</span>
    </li>
  </ul>

  <div class="headshot" role="img" aria-label="Headshot photo of the agent in a blue suit"></div>

  <div class="nameplate">
    <svg viewBox="0 0 257 65" width="257" height="65"><polygon points="0,65 59,0 257,0 257,65" fill="var(--olive)"/></svg>
    <div class="nameplate__text">
      <p class="nameplate__name">DANIEL REYES</p>
      <p class="nameplate__title">CEO/FOUNDER</p>
    </div>
  </div>
</section>

<section class="card card--back">
  <div class="brand">
    <span class="brand__mark"></span>
    <span class="brand__name">Harbor<br>Crest<br>Realty</span>
  </div>
  <p class="website">www.harborcrestrealty.com</p>
</section>

</body>
</html>
```